Retirement maintenance and reinstatment brochure

We are looking for a capability statement/brochure outlining our skills and capabilities for maintenance, reinstatement and refurbishment work specific to the requirements of retirement villages in Australia

We are a new company, however our people have significant experience working in this industry

Target Market(s)

Retirement living facilities, aged care facilities, hospitals

Industry/Entity Type

Building

Colors

Designer to choose colors to be used in the design.

Requirements
Must have
• Not alot of wording. Stock images of building refurbishment to retirement living and aged care (carpenters, painters etc)
Nice to have
• 1-2 pages only
Should not have
• alot of meaningless writing

```html
<!DOCTYPE html>
<html lang="en">
<head>
<meta charset="utf-8">
<title>Keystone Care – Capability Brochure</title>
<link rel="stylesheet" href="https://fonts.googleapis.com/css2?family=Oswald:wght@500&family=Open+Sans:wght@400;600&display=swap">
<style>
  :root {
    --backdrop: #2b2b2d;
    --paper: #ffffff;
    --paper-grey: #e4e6ea;
    --navy: #27497a;
    --blue: #2f62ae;
    --red: #d3272f;
    --ink: #3a3d44;
    --muted: #6b6f78;
    --photo-warm: #c9b69e;
    --photo-cool: #9aa3ad;
  }
  * { box-sizing: border-box; margin: 0; padding: 0; }
  html, body { width: 1200px; height: 720px; overflow: hidden; }
  body {
    background: var(--backdrop);
    font-family: "Open Sans", Arial, sans-serif;
    color: var(--ink);
  }
  .spread {
    position: absolute; left: 133px; top: 30px;
    width: 934px; height: 660px;
    box-shadow: 0 12px 40px rgba(0,0,0,.5);
  }
  .page { position: absolute; top: 0; width: 467px; height: 660px; }
  .page--back { left: 0; background: linear-gradient(160deg, #f1f2f4, var(--paper-grey)); }
  .page--front { left: 467px; background: var(--paper); }
  .artwork { position: absolute; inset: 0; width: 934px; height: 660px; }
  .layer { position: absolute; inset: 0; }

  .brand { position: absolute; display: flex; align-items: center; gap: 10px; }
  .brand__dot { width: 26px; height: 26px; border-radius: 50%; background: var(--blue); }
  .brand__name {
    font-family: "Oswald", Arial, sans-serif; font-weight: 500;
    font-size: 30px; letter-spacing: .5px; color: var(--navy);
  }

  .back-brand { left: 120px; top: 380px; }
  .back-copy {
    position: absolute; left: 150px; top: 470px; width: 290px;
    font-size: 10.5px; line-height: 1.55; color: var(--muted); text-align: right;
  }
  .back-rule { position: absolute; left: 24px; right: 24px; top: 560px; height: 2px; background: var(--navy); }
  .contact-row {
    position: absolute; left: 24px; right: 24px; top: 580px;
    display: flex; align-items: center; justify-content: space-between;
    font-size: 11px; color: var(--ink);
  }
  .contact-row__item { display: flex; align-items: center; gap: 6px; }
  .contact-row__sep { width: 2px; height: 16px; background: var(--red); }
  .icon { width: 12px; height: 12px; fill: var(--navy); }

  .front-brand { right: 40px; top: 478px; }
  .front-tagline {
    position: absolute; left: 30px; right: 30px; top: 540px;
    font-size: 12.5px; font-weight: 600; letter-spacing: .4px; text-align: right;
    color: var(--ink); padding-bottom: 8px; border-bottom: 2px solid var(--red);
  }
  .front-web {
    position: absolute; right: 30px; top: 578px;
    display: flex; align-items: center; gap: 6px; font-size: 12px; color: var(--ink);
  }
</style>
</head>
<body>
<div class="spread">
  <div class="page page--back"></div>
  <div class="page page--front"></div>

  <svg class="artwork" viewBox="0 0 934 660" xmlns="http://www.w3.org/2000/svg">
    <defs>
      <clipPath id="front-photo-clip">
        <rect x="467" y="0" width="467" height="660"/>
      </clipPath>
      <linearGradient id="couple-tone" x1="0" y1="0" x2="1" y2="1">
        <stop offset="0" stop-color="#e9e6e2"/>
        <stop offset=".55" stop-color="var(--photo-cool)"/>
        <stop offset="1" stop-color="#6f7c8c"/>
      </linearGradient>
      <linearGradient id="carpenter-tone" x1="0" y1="0" x2="1" y2="1">
        <stop offset="0" stop-color="#e2d3bd"/>
        <stop offset="1" stop-color="var(--photo-warm)"/>
      </linearGradient>
    </defs>

    <g role="img" aria-label="Photo of a smiling retired couple sitting together on a sofa at home" clip-path="url(#front-photo-clip)">
      <circle cx="560" cy="60" r="322" fill="url(#couple-tone)"/>
    </g>

    <path class="arc-light" d="M 240 -60 A 360 360 0 0 0 320 340" fill="none" stroke="#d6dce6" stroke-width="10"/>
    <path class="arc-band" d="M 252 -84 A 340 340 0 1 0 868 204" fill="none" stroke="var(--navy)" stroke-width="36"/>
    <polygon class="arc-head" points="897,130 912,226 826,186" fill="var(--navy)"/>

    <g role="img" aria-label="Photo of a carpenter measuring and marking timber flooring">
      <circle cx="330" cy="230" r="92" fill="url(#carpenter-tone)" stroke="var(--red)" stroke-width="3"/>
    </g>
  </svg>

  <div class="layer">
    <div class="brand back-brand">
      <span class="brand__dot"></span>
      <span class="brand__name">KEYSTONE CARE</span>
    </div>
    <p class="back-copy">Lorem ipsum dolor sit amet, consectetur adipiscing elit, sed do eiusmod tempor incididunt ut labore et dolore magna aliqua. Ut enim ad minim veniam, quis nostrud exercitation ullamco laboris nisi ut aliquip ex ea commodo consequat.</p>
    <div class="back-rule"></div>
    <div class="contact-row" style="width:419px">
      <span class="contact-row__item">
        <svg class="icon" viewBox="0 0 12 12"><path d="M6 0a4 4 0 0 0-4 4c0 3 4 8 4 8s4-5 4-8a4 4 0 0 0-4-4zm0 5.5A1.5 1.5 0 1 1 6 2.5a1.5 1.5 0 0 1 0 3z"/></svg>
        48 Harbour Rd. Geelong, VIC 3220
      </span>
      <span class="contact-row__sep"></span>
      <span class="contact-row__item">
        <svg class="icon" viewBox="0 0 12 12"><path d="M2.5 0.5l2 2.5-1.2 1.5a7 7 0 0 0 4.2 4.2L9 7.5l2.5 2-1.5 2C5 11.5.5 7 .5 2z"/></svg>
        555-014-288
      </span>
      <span class="contact-row__sep"></span>
      <span class="contact-row__item">
        <svg class="icon" viewBox="0 0 12 12"><circle cx="6" cy="6" r="5.5"/></svg>
        www.keystonecare.example
      </span>
    </div>

    <div class="brand front-brand">
      <span class="brand__dot"></span>
      <span class="brand__name">KEYSTONE CARE</span>
    </div>
    <p class="front-tagline">LOREM IPSUM DOLOR SIT AMET, CONSECTETUR ADIPISCING ELIT</p>
    <div class="front-web">
      <svg class="icon" viewBox="0 0 12 12"><circle cx="6" cy="6" r="5.5"/></svg>
      www.keystonecare.example
    </div>
  </div>
</div>
</body>
</html>
```